Strength Coach Business Card Design Project

I would like a business card design to complement my new logo. I would like the card to be clean, seek and strong!

Target Market(s)

Mostly adults and junior atheletes who are serious about changing their lives.

Industry/Entity Type

Business

Font styles to use
Serif

Colors

Designer to choose colors to be used in the design.

```html
<!DOCTYPE html>
<html lang="en">
<head>
<meta charset="utf-8">
<title>Ridgeline Strength &amp; Fitness – Business Card</title>
<link rel="stylesheet" href="https://fonts.googleapis.com/css2?family=Barlow:wght@500;600;700&display=swap">
<style>
  :root {
    --backdrop: #c8c8c8;
    --paper: #ffffff;
    --ink: #2b2a2c;
    --ink-deep: #1d1c1e;
    --rule-dark: #3b3a3c;
    --red: #e42127;
    --red-deep: #b51b23;
    --muted: #bdbdbd;
    --white: #ffffff;
  }
  * { margin: 0; padding: 0; box-sizing: border-box; }
  html, body {
    width: 840px; height: 1200px; overflow: hidden;
    background: var(--backdrop);
    font-family: "Barlow", Arial, sans-serif;
  }
  .canvas { position: relative; width: 840px; height: 1200px; }
  .business-card {
    position: absolute; left: 115px; top: 128px;
    width: 608px; height: 367px; overflow: hidden;
    background: var(--paper);
  }
  .card-shapes { position: absolute; inset: 0; }
  .brand {
    position: absolute; left: 36px; top: 50px;
    display: flex; align-items: center; gap: 16px;
  }
  .brand-mark { width: 62px; height: 62px; background: var(--red); }
  .brand-name {
    color: var(--ink); font-weight: 700; font-size: 24px;
    line-height: 1.05; letter-spacing: 1px; text-transform: uppercase;
  }
  .holder { position: absolute; left: 390px; top: 144px; width: 160px; text-align: center; }
  .holder-name { color: var(--white); font-weight: 700; font-size: 25px; line-height: 1; letter-spacing: .3px; }
  .holder-role { color: var(--muted); font-weight: 600; font-size: 15px; letter-spacing: 1px; margin-top: 5px; }
  .contact {
    position: absolute; display: flex; align-items: center; gap: 10px;
    color: var(--white); font-weight: 600; font-size: 17px; letter-spacing: .5px;
  }
  .contact svg { flex: none; }
  .contact.phone { left: 36px; top: 236px; }
  .contact.fax { left: 32px; top: 272px; }
  .contact.email { left: 214px; top: 236px; }
  .contact.web { left: 215px; top: 270px; }
  .contact.address { left: 34px; top: 320px; color: var(--muted); }
</style>
</head>
<body>
<main class="canvas">
  <section class="business-card">
    <svg class="card-shapes" viewBox="0 0 608 367" width="608" height="367" aria-hidden="true">
      <defs>
        <linearGradient id="inkFade" x1="0" y1="0" x2="1" y2="1">
          <stop offset="0" stop-color="#2b2a2c"/>
          <stop offset="1" stop-color="#1d1c1e"/>
        </linearGradient>
        <linearGradient id="redFade" x1="0" y1="0" x2="1" y2="0">
          <stop offset="0" stop-color="#e42127"/>
          <stop offset="1" stop-color="#b51b23"/>
        </linearGradient>
      </defs>
      <path class="dark-field" d="M312 139 H608 V367 H0 V205 H330 Z" fill="url(#inkFade)"/>
      <line x1="485" y1="213" x2="608" y2="213" stroke="#3b3a3c" stroke-width="1.5"/>
      <polygon class="red-stripe" points="0,197 318,197 321,201 0,201" fill="#e42127"/>
      <path class="band-outline" d="M0 207 H470 Q489 207 489 226 V280 Q489 310 459 310 H0 Z" fill="#ffffff"/>
      <path class="contact-band" d="M0 211 H468 Q485 211 485 228 V279 Q485 306 458 306 H0 Z" fill="url(#redFade)"/>
      <g class="user-icon">
        <rect x="345" y="144" width="32" height="28" fill="#ffffff"/>
        <circle cx="361" cy="153" r="5" fill="#2b2a2c"/>
        <path d="M350 172 Q350 160 361 160 Q372 160 372 172 Z" fill="#2b2a2c"/>
      </g>
    </svg>

    <div class="brand">
      <div class="brand-mark"></div>
      <div class="brand-name">Ridgeline<br>Strength &amp; Fitness</div>
    </div>

    <div class="holder">
      <div class="holder-name">YOUR NAME</div>
      <div class="holder-role">DESIGNATION</div>
    </div>

    <div class="contact phone">
      <svg width="14" height="22" viewBox="0 0 14 22"><rect x="1" y="1" width="12" height="20" rx="2" fill="none" stroke="#fff" stroke-width="2"/><rect x="4" y="4" width="6" height="6" fill="#fff"/><rect x="4" y="13" width="6" height="4" fill="#fff"/></svg>
      <span>0194 XXX XXX</span>
    </div>
    <div class="contact fax">
      <svg width="20" height="18" viewBox="0 0 20 18"><rect x="5" y="0" width="10" height="5" fill="#fff"/><rect x="0" y="6" width="20" height="8" rx="2" fill="#fff"/><rect x="5" y="12" width="10" height="6" fill="#fff" stroke="#c81e25" stroke-width="1"/></svg>
      <span>0194 XXX XXX</span>
    </div>
    <div class="contact email">
      <svg width="24" height="16" viewBox="0 0 24 16"><rect width="24" height="16" fill="#fff"/><path d="M1 1 L12 9 L23 1" fill="none" stroke="#c81e25" stroke-width="1.6"/></svg>
      <span>info@email.com</span>
    </div>
    <div class="contact web">
      <svg width="20" height="20" viewBox="0 0 20 20" fill="none" stroke="#fff" stroke-width="1.5"><circle cx="10" cy="10" r="8.5"/><ellipse cx="10" cy="10" rx="3.8" ry="8.5"/><line x1="1.5" y1="10" x2="18.5" y2="10"/><path d="M3 5.5 H17 M3 14.5 H17"/></svg>
      <span>www.web.com</span>
    </div>
    <div class="contact address">
      <svg width="14" height="22" viewBox="0 0 14 22"><path d="M7 0 A7 7 0 0 1 14 7 C14 12 7 22 7 22 C7 22 0 12 0 7 A7 7 0 0 1 7 0 Z" fill="#fff"/><circle cx="7" cy="7" r="2.6" fill="#2b2a2c"/></svg>
      <span>YOUR ADDRESS</span>
    </div>
  </section>
</main>
</body>
</html>
```